Personal Injury Law Firm Marketing Postcards

Looking for 4 different high quality graphic postcards (print on both sides of 4"x6" postcard to market a Personal Injury Lawyer (Walter Dunmore). These will be placed on cars and in stores on stands. My photo and/or stock images.... We are targeting People who have been injured in automobile accidents, motorcycle accidents, slip and fall (wet/greasy floors indoors in supermarkets, restaurants, etc., snow and ice outdoors on sidewalks) trip and fall cases on dangerous staircases. indoor/outdoor, dog bite injuries. ( I like the use of stock images of these type of injury causing accidents. You can use following language "Serving People Injured in NY & NJ" . Millions of Dollars Recovered, Free Consultation and No Fee Unless We Recover Money! Phone number to be displayed (555) 614-3082 "call or text" Available 24 hours a day 7 days per week. May also want to mention that we can take over your case from another lawyer if you are not satisfied with your current attorney. There should be a small space in corner which has a space for my marketing person to handwrite in their reference code.

Target Market(s)

18-75 years old - densely populated major city

Industry/Entity Type

Legal

Font styles to use
Other font styles liked:
• Please use logo style that I uploaded.. Please do not just cut parts of my website out and use them. Do not use LOGO from my website

Colors
0054AA
0677BA
7BADD7
CADEEF
E8F1F8
00AB8E
00BBA5
67D7C9
C6EFE9
E9F9F6

Requirements
Must have
• Professional Appearance

```html
<!DOCTYPE html>
<html lang="en">
<head>
<meta charset="utf-8">
<title>Walter Dunmore Injury Postcards</title>
<link href="https://fonts.googleapis.com/css2?family=Montserrat:wght@500;600;700;800;900&display=swap" rel="stylesheet">
<style>
:root{
  --blue:#0054AA;
  --blue-dark:#0a3f86;
  --blue-mid:#0677BA;
  --blue-light:#7BADD7;
  --blue-pale:#CADEEF;
  --ice:#E8F1F8;
  --white:#ffffff;
  --gold:#a88a4a;
  --stage:#e9ecef;
}
*{box-sizing:border-box;margin:0;padding:0}
html,body{width:1200px;height:800px;overflow:hidden}
body{background:var(--stage);font-family:"Montserrat",sans-serif;position:relative}
.card{position:absolute;width:570px;height:380px;overflow:hidden;background:var(--white);box-shadow:0 6px 18px rgba(0,0,0,.18)}
.card--front{left:20px;top:210px}
.card--back{left:610px;top:210px}
.abs{position:absolute}

/* front */
.front-scene{left:0;top:0;width:570px;height:250px;background:linear-gradient(180deg,#9fb6d4 0%,#5d7fae 45%,#3c5f94 100%)}
.front-portrait{left:55px;top:35px;width:170px;height:215px;background:radial-gradient(ellipse at 50% 30%,#7a6a5e 0%,#3d3f52 45%,#2b3658 100%)}
.front-car{left:235px;top:140px;width:250px;height:150px;background:radial-gradient(ellipse at 50% 55%,#f6f7f8 0%,#d9dde2 55%,rgba(255,255,255,0) 75%)}
.headline{left:213px;top:0;width:257px;height:150px;background:var(--blue);color:var(--white);padding:18px 14px 0;text-align:center;border-left:2px dashed var(--blue-light);border-right:2px dashed var(--blue-light)}
.headline__big{font-size:38px;font-weight:900;line-height:1}
.headline__sub{font-size:21px;font-weight:800;line-height:1.15;padding-bottom:6px;border-bottom:2px solid var(--white)}
.headline__call{margin-top:9px;background:var(--white);color:var(--blue);font-size:15px;font-weight:900;padding:6px 4px;white-space:nowrap}
.phone-strip{right:18px;top:48px;width:32px;height:170px;background:var(--white);display:flex;align-items:center;justify-content:center}
.phone-strip span{transform:rotate(90deg);white-space:nowrap;font-size:17px;font-weight:900;color:var(--blue)}
.phone-strip__icon{right:18px;top:18px;width:32px;height:30px;background:var(--blue);display:flex;align-items:center;justify-content:center}
.ribbon{background:var(--white);clip-path:polygon(0 0,100% 0,100% 100%,50% 86%,0 100%);border:1px dashed var(--blue-light);display:flex;align-items:center;justify-content:center;text-align:center;color:var(--gold);font-weight:700;line-height:1.2}
.ribbon--front{left:10px;top:30px;width:78px;height:78px;font-size:8px;padding:0 4px 10px}
.name-tag{background:var(--white);color:var(--blue);font-weight:900;padding:4px 8px;white-space:nowrap}
.name-tag--front{left:22px;top:214px;font-size:16px}
.tab{left:22px;top:259px;background:var(--blue);color:var(--white);font-size:12px;font-weight:800;padding:5px 22px 5px 8px;clip-path:polygon(0 0,100% 0,92% 100%,0 100%)}
.checks{list-style:none;color:var(--blue);font-weight:700}
.checks li{display:flex;align-items:flex-start;gap:6px}
.checks svg{flex:0 0 auto;margin-top:2px}
.checks--front{left:26px;top:288px;width:240px;font-size:11px;line-height:1.2}
.checks--front li{margin-bottom:3px}
.footer-band{left:0;top:356px;width:570px;height:24px;background:var(--blue);color:var(--white);display:flex;align-items:center}
.footer-band__main{font-size:12px;font-weight:700;padding:0 14px;border-right:2px solid var(--white);height:100%;display:flex;align-items:center;white-space:nowrap}
.footer-band__note{font-size:6.5px;font-weight:600;padding:0 12px;line-height:1.2;text-transform:uppercase}
.clock{display:flex;align-items:center;gap:3px;color:var(--blue);font-weight:900;line-height:.95}
.clock small{display:block;font-size:7px;font-weight:700}
.clock b{display:block;font-size:10px}
.clock--front{right:14px;top:300px}

/* back */
.back-panel{left:0;top:0;width:310px;height:380px;background:linear-gradient(160deg,#2a5fa8 0%,var(--blue) 40%,var(--blue-dark) 100%)}
.back-portrait{left:0;top:200px;width:175px;height:180px;background:radial-gradient(ellipse at 50% 30%,#7a6a5e 0%,#3b405a 45%,#223560 100%)}
.ribbon--back{left:8px;top:0;width:62px;height:62px;font-size:6.5px;padding:0 3px 8px}
.back-title{left:80px;top:14px;color:var(--white);font-size:15px;font-weight:900;line-height:1.05;display:flex;gap:6px}
.back-label{left:80px;top:86px;color:var(--white);font-size:12px;font-weight:700}
.back-phone{left:60px;top:104px;color:var(--white);font-size:26px;font-weight:800;white-space:nowrap}
.checks--back{left:88px;top:150px;color:var(--white);font-size:11px;line-height:1.15}
.checks--back li{margin-bottom:6px}
.name-tag--back{left:178px;top:306px;font-size:12px}
.clock--back{left:210px;top:338px;color:var(--white)}
.stamp{right:16px;top:22px;width:60px;height:72px;border:1px solid #555}
.addr-line{left:330px;width:220px;height:1px;background:#555}
</style>
</head>
<body>

<section class="card card--front">
  <div class="abs front-scene" role="img" aria-label="Blurred city buildings under a blue sky"></div>
  <div class="abs front-portrait" role="img" aria-label="Portrait of the attorney in a navy suit, hand at chin"></div>
  <div class="abs front-car" role="img" aria-label="White compact car with a crushed front end"></div>

  <div class="abs ribbon ribbon--front">Law Office of Walter Dunmore P.C.</div>

  <div class="abs headline">
    <div class="headline__big">INJURED?</div>
    <div class="headline__sub">IN AN ACCIDENT</div>
    <div class="headline__call">CALL WALTER DUNMORE</div>
  </div>

  <div class="abs phone-strip__icon">
    <svg width="16" height="16" viewBox="0 0 24 24"><path fill="#fff" d="M6.6 10.8a15.1 15.1 0 0 0 6.6 6.6l2.2-2.2a1 1 0 0 1 1-.25 11.4 11.4 0 0 0 3.6.57 1 1 0 0 1 1 1V20a1 1 0 0 1-1 1A17 17 0 0 1 3 4a1 1 0 0 1 1-1h3.5a1 1 0 0 1 1 1c0 1.25.2 2.45.57 3.57a1 1 0 0 1-.25 1z"/></svg>
  </div>
  <div class="abs phone-strip"><span>(555) 614-3082</span></div>

  <div class="abs name-tag name-tag--front">WALTER DUNMORE</div>

  <div class="abs tab">FREE CONSULTATION</div>
  <ul class="abs checks checks--front">
    <li><svg width="10" height="10" viewBox="0 0 10 10"><rect width="10" height="10" fill="#0054AA"/><path d="M2 5l2 2 4-4" stroke="#fff" stroke-width="1.6" fill="none"/></svg>Over 10 Years Experience</li>
    <li><svg width="10" height="10" viewBox="0 0 10 10"><rect width="10" height="10" fill="#0054AA"/><path d="M2 5l2 2 4-4" stroke="#fff" stroke-width="1.6" fill="none"/></svg>No Fee Unless We Recover Money!</li>
    <li><svg width="10" height="10" viewBox="0 0 10 10"><rect width="10" height="10" fill="#0054AA"/><path d="M2 5l2 2 4-4" stroke="#fff" stroke-width="1.6" fill="none"/></svg><span>Millions of Dollars Recovered for<br>Our Clients</span></li>
  </ul>

  <div class="abs clock clock--front">
    <svg width="34" height="36" viewBox="0 0 34 36"><rect x="14" y="0" width="6" height="4" fill="#0054AA"/><circle cx="17" cy="20" r="14" fill="none" stroke="#0054AA" stroke-width="3"/><text x="17" y="25" text-anchor="middle" font-family="Montserrat,sans-serif" font-weight="900" font-size="14" fill="#0054AA">24</text></svg>
    <div><b>HOURS</b><small>SERVICE</small><b>7 DAYS</b><small>PER WEEK</small></div>
  </div>

  <div class="abs footer-band">
    <div class="footer-band__main">Serving People Injured in NY &amp; NJ</div>
    <div class="footer-band__note">We can take over your case from another lawyer if you<br>are not satisfied with your current attorney.</div>
  </div>
</section>

<section class="card card--back">
  <div class="abs back-panel"></div>
  <div class="abs back-portrait" role="img" aria-label="Portrait of the attorney in a navy suit, hand at chin"></div>
  <div class="abs ribbon ribbon--back">Law Office of Walter Dunmore P.C.</div>

  <div class="abs back-title">
    <svg width="20" height="20" viewBox="0 0 24 24"><path fill="#fff" d="M6.6 10.8a15.1 15.1 0 0 0 6.6 6.6l2.2-2.2a1 1 0 0 1 1-.25 11.4 11.4 0 0 0 3.6.57 1 1 0 0 1 1 1V20a1 1 0 0 1-1 1A17 17 0 0 1 3 4a1 1 0 0 1 1-1h3.5a1 1 0 0 1 1 1c0 1.250.2 2.45.57 3.57a1 1 0 0 1-.25 1z"/></svg>
    <span>CALL US FOR FREE<br>CONSULTATION!</span>
  </div>
  <div class="abs back-label">PHONE NUMBER :</div>
  <div class="abs back-phone">(555) 614-3082</div>

  <ul class="abs checks checks--back">
    <li><svg width="10" height="10" viewBox="0 0 10 10"><rect width="10" height="10" fill="#fff"/><path d="M2 5l2 2 4-4" stroke="#0054AA" stroke-width="1.6" fill="none"/></svg>Over 10 Years Experience</li>
    <li><svg width="10" height="10" viewBox="0 0 10 10"><rect width="10" height="10" fill="#fff"/><path d="M2 5l2 2 4-4" stroke="#0054AA" stroke-width="1.6" fill="none"/></svg><span>No Fee Unless We<br>Recover Money!</span></li>
    <li><svg width="10" height="10" viewBox="0 0 10 10"><rect width="10" height="10" fill="#fff"/><path d="M2 5l2 2 4-4" stroke="#0054AA" stroke-width="1.6" fill="none"/></svg><span>Millions of Dollars<br>Recovered Our Clients</span></li>
  </ul>

  <div class="abs name-tag name-tag--back">WALTER DUNMORE</div>
  <div class="abs clock clock--back">
    <svg width="30" height="32" viewBox="0 0 34 36"><rect x="14" y="0" width="6" height="4" fill="#fff"/><circle cx="17" cy="20" r="14" fill="none" stroke="#fff" stroke-width="3"/><text x="17" y="25" text-anchor="middle" font-family="Montserrat,sans-serif" font-weight="900" font-size="14" fill="#fff">24</text></svg>
    <div><b>HOURS</b><small>SERVICE</small><b>7 DAYS</b><small>PER WEEK</small></div>
  </div>

  <div class="abs stamp"></div>
  <div class="abs addr-line" style="top:150px"></div>
  <div class="abs addr-line" style="top:190px"></div>
  <div class="abs addr-line" style="top:230px"></div>
  <div class="abs addr-line" style="top:270px"></div>
  <div class="abs addr-line" style="top:310px"></div>
  <div class="abs addr-line" style="top:350px"></div>
</section>

</body>
</html>
```